Business Card Design needed for logo design project

Would like a professional business card for a company involved in financial and latest technologies including CAD design. We would like the card to convey professionalism and communicate that we are involved in up to date technology solutions.

Target Market(s)

Business 2 Business sales

Industry/Entity Type

Financial

Colors

Designer to choose colors to be used in the design.

Requirements
Must have
• Business Name
Logo
Name
Phone
Email
Nice to have
• Website

```html
<!DOCTYPE html>
<html lang="en">
<head>
<meta charset="utf-8">
<title>Veltrix Business Card</title>
<link rel="stylesheet" href="https://fonts.googleapis.com/css2?family=Arimo:wght@400;700&display=swap">
<style>
  :root {
    --page-bg: #e9e9ec;
    --navy: #1c2340;
    --navy-deep: #0f1428;
    --red: #d22a2f;
    --white: #ffffff;
    --ink: #1c2340;
  }
  * { box-sizing: border-box; margin: 0; padding: 0; }
  html, body { width: 1200px; height: 784px; overflow: hidden; }
  body {
    background: var(--page-bg);
    font-family: "Arimo", Arial, sans-serif;
    position: relative;
  }
  .card {
    position: absolute;
    top: 232px;
    width: 560px;
    height: 320px;
    overflow: hidden;
    box-shadow: 0 6px 18px rgba(0,0,0,0.18);
  }
  .card-back {
    left: 30px;
    background: radial-gradient(ellipse at 50% 40%, #2a3358 0%, var(--navy) 55%, var(--navy-deep) 100%);
    display: flex;
    align-items: center;
    justify-content: center;
  }
  .card-front { left: 610px; background: var(--white); }
  .brand-name {
    font-family: "Arimo", Arial, sans-serif;
    font-weight: 700;
    letter-spacing: 2px;
    line-height: 1;
  }
  .card-back .brand-name { color: var(--white); font-size: 64px; }
  .card-front .brand-name {
    position: absolute;
    left: 70px;
    top: 62px;
    color: var(--red);
    font-size: 50px;
  }
  .holder { position: absolute; left: 80px; top: 138px; }
  .holder-name { color: var(--red); font-size: 20px; font-weight: 400; line-height: 22px; }
  .holder-title { color: var(--ink); font-size: 11px; font-weight: 700; margin-top: 2px; }
  .contact-list {
    position: absolute;
    left: 80px;
    top: 180px;
    list-style: none;
    color: var(--ink);
    font-size: 13.5px;
    line-height: 17px;
  }
  .contact-list li { display: flex; align-items: center; gap: 5px; }
  .contact-list li.indent { padding-left: 19px; }
  .contact-icon { width: 14px; height: 14px; flex: none; }
  .footer-band { position: absolute; left: 0; bottom: 0; }
</style>
</head>
<body>
  <section class="card card-back">
    <span class="brand-name">VELTRIX</span>
  </section>

  <section class="card card-front">
    <span class="brand-name">VELTRIX</span>

    <div class="holder">
      <p class="holder-name">Dane Carter</p>
      <p class="holder-title">Manager</p>
    </div>

    <ul class="contact-list">
      <li>
        <svg class="contact-icon" viewBox="0 0 16 16"><path fill="#d22a2f" d="M3.5 1.5l2.5 0 1 3.5-1.6 1.2c.8 1.8 2.1 3.1 3.9 3.9L10.5 8.5 14 9.5v2.5c0 1-1 2-2 2C6.5 14 2 9.5 2 4c0-1 .5-2.5 1.5-2.5z"/></svg>
        555-014-2280
      </li>
      <li>
        <svg class="contact-icon" viewBox="0 0 16 16"><rect x="1.5" y="3.5" width="13" height="9" rx="1" fill="#d22a2f"/><path d="M2 4l6 5 6-5" stroke="#fff" stroke-width="1.3" fill="none"/></svg>
        info@veltrix.com
      </li>
      <li>
        <svg class="contact-icon" viewBox="0 0 16 16"><circle cx="8" cy="8" r="6.5" fill="#d22a2f"/><path d="M1.5 8h13M8 1.5v13M3 4.5h10M3 11.5h10" stroke="#fff" stroke-width="1"/><ellipse cx="8" cy="8" rx="3" ry="6.5" stroke="#fff" stroke-width="1" fill="none"/></svg>
        www.veltrix.com
      </li>
      <li>
        <svg class="contact-icon" viewBox="0 0 16 16"><path fill="#d22a2f" d="M8 1.5L1 8h2v6.5h4v-4h2v4h4V8h2z"/></svg>
        4820 W. Meridian Road,
      </li>
      <li class="indent">Austin, Texas 73301</li>
    </ul>

    <svg class="footer-band" width="560" height="50" viewBox="0 0 560 50" aria-hidden="true">
      <line x1="0" y1="28" x2="560" y2="6" stroke="#d22a2f" stroke-width="2.5"/>
      <polygon points="0,34 560,12 560,50 0,50" fill="#1c2340"/>
    </svg>
  </section>
</body>
</html>
```